Business Card design for shipping company 'FERNHOLT INTERNATIONAL LTD'

Classic / traditional business card in black Garamond / Times New Roman or similar text for a shipping / marine transport company, containing the following information:

QUOTE

FERNHOLT INTERNATIONAL LTD

MARTIN QUESTEDGE FICS

T: +44 7902 615370
E: cargo@fernholt-example.com

UNQUOTE

Target Market(s)

Marine / Shipping industry

Contact Information for Business Card

FERNHOLT INTERNATIONAL LTD MARTIN QUESTEDGE FICS T: +44 7902 615370 E: cargo@fernholt-example.com

Font styles to use
Serif

Colors

Designer to choose colors to be used in the design.

Requirements
Must have
• Garamond / Times New Roman or similar text in black colour

```html
<!DOCTYPE html>
<html lang="en">
<head>
<meta charset="utf-8">
<title>Fernholt International Ltd – Business Card</title>
<link rel="stylesheet" href="https://fonts.googleapis.com/css2?family=EB+Garamond:wght@400;600;700;800&display=swap">
<style>
  :root {
    --ink: #000000;
    --paper: #ffffff;
    --canvas-bg: #f4f5f7;
    --blue-deep: #0053a6;
    --blue-mid: #0a67b4;
    --blue-bright: #1b7ec6;
    --blue-pale: #86bce4;
    --band-blue: #0a78bf;
    --mist-light: #fbfbfb;
    --mist-dark: #e4e5e7;
  }
  * { margin: 0; padding: 0; box-sizing: border-box; }
  html, body { width: 1200px; height: 1200px; overflow: hidden; }
  body {
    background: var(--canvas-bg);
    font-family: "EB Garamond", "Times New Roman", serif;
    color: var(--ink);
    position: relative;
  }
  .card {
    position: absolute;
    left: 157px;
    width: 886px;
    height: 507px;
    overflow: hidden;
    background: var(--paper);
  }
  .card--front { top: 66px; }
  .card--back { top: 634px; }
  .card__art { position: absolute; inset: 0; width: 100%; height: 100%; }

  .holder { position: absolute; left: 61px; top: 88px; width: 440px; }
  .holder__name {
    font-weight: 800;
    font-size: 40px;
    line-height: 1;
    letter-spacing: 0.6px;
    white-space: nowrap;
  }
  .holder__role {
    font-weight: 400;
    font-size: 24px;
    margin-top: 8px;
    letter-spacing: 0.3px;
  }
  .holder__rule {
    height: 2px;
    background: var(--ink);
    margin-top: 13px;
  }

  .contacts { position: absolute; left: 62px; top: 249px; list-style: none; }
  .contacts__item {
    display: flex;
    align-items: center;
    height: 40px;
    margin-bottom: 20px;
    font-weight: 700;
    font-size: 25px;
    letter-spacing: 0.4px;
    white-space: nowrap;
  }
  .contacts__icon { width: 40px; height: 40px; margin-right: 18px; flex: none; }

  .company {
    position: absolute;
    left: 0; right: 0; top: 190px;
    text-align: center;
    font-weight: 800;
    font-size: 50px;
    line-height: 50px;
    letter-spacing: 1px;
  }
  .band { position: absolute; left: 0; top: 0; width: 100%; height: 25px; background: var(--band-blue); }
</style>
</head>
<body>

<section class="card card--front">
  <svg class="card__art" viewBox="0 0 886 507" preserveAspectRatio="none">
    <defs>
      <linearGradient id="mist-front" x1="0" y1="0" x2="1" y2="0">
        <stop offset="0" stop-color="var(--paper)"/>
        <stop offset="0.55" stop-color="var(--mist-light)"/>
        <stop offset="1" stop-color="var(--mist-dark)"/>
      </linearGradient>
    </defs>
    <rect width="886" height="507" fill="url(#mist-front)" role="img" aria-label="Faint background photo of a container ship over a world network map"/>
    <path d="M0,0 L83,0 C45,25 18,55 0,87 Z" fill="var(--blue-pale)"/>
    <path d="M0,0 L75,0 C40,22 15,45 0,68 Z" fill="var(--blue-mid)"/>
    <path d="M0,430 C160,478 600,462 886,134 L886,507 L0,507 Z" fill="var(--blue-pale)"/>
    <path d="M0,435 C160,485 600,470 886,157 L886,507 L0,507 Z" fill="var(--blue-deep)"/>
    <path d="M0,470 C200,500 560,470 886,255 L886,507 L0,507 Z" fill="var(--blue-mid)"/>
    <path d="M0,480 C220,505 500,490 886,330 L886,507 L0,507 Z" fill="var(--blue-bright)" opacity="0.45"/>
  </svg>

  <div class="holder">
    <h1 class="holder__name">MARTIN QUESTEDGE FICS</h1>
    <p class="holder__role">Head of Director</p>
    <div class="holder__rule"></div>
  </div>

  <ul class="contacts">
    <li class="contacts__item">
      <svg class="contacts__icon" viewBox="0 0 40 40">
        <circle cx="20" cy="20" r="20" fill="var(--blue-deep)"/>
        <path d="M13.5,11 L17,11 L18.5,15.5 L16.3,17.2 C17.4,19.7 19.6,22 22.2,23.2 L24,21 L28.5,22.5 L28.5,26 C28.5,27.4 27.4,28.5 26,28.5 C18.5,28.2 11.8,21.5 11.5,14 C11.5,12.3 12.3,11 13.5,11 Z" fill="none" stroke="var(--paper)" stroke-width="1.8" stroke-linejoin="round"/>
        <path d="M21.5,12 A6.5,6.5 0 0 1 28,18.5 M21.5,15.2 A3.3,3.3 0 0 1 24.8,18.5" fill="none" stroke="var(--paper)" stroke-width="1.6" stroke-linecap="round"/>
      </svg>
      <span>+44 7902 615370</span>
    </li>
    <li class="contacts__item">
      <svg class="contacts__icon" viewBox="0 0 40 40">
        <circle cx="20" cy="20" r="20" fill="var(--blue-deep)"/>
        <rect x="10" y="13" width="20" height="14" fill="none" stroke="var(--paper)" stroke-width="1.8"/>
        <path d="M10,13 L20,21 L30,13 M10,27 L17,19.5 M30,27 L23,19.5" fill="none" stroke="var(--paper)" stroke-width="1.6"/>
      </svg>
      <span>cargo@fernholt-example.com</span>
    </li>
  </ul>
</section>

<section class="card card--back">
  <svg class="card__art" viewBox="0 0 886 507" preserveAspectRatio="none">
    <defs>
      <radialGradient id="mist-back" cx="0.5" cy="0.45" r="0.7">
        <stop offset="0" stop-color="var(--paper)"/>
        <stop offset="0.6" stop-color="var(--mist-light)"/>
        <stop offset="1" stop-color="var(--mist-dark)"/>
      </radialGradient>
    </defs>
    <rect width="886" height="507" fill="url(#mist-back)" role="img" aria-label="Faint background photo of a container ship over a world network map"/>
    <path d="M0,366 C250,470 600,470 886,335 L886,507 L0,507 Z" fill="var(--blue-pale)"/>
    <path d="M0,366 C250,475 600,470 886,357 L886,507 L0,507 Z" fill="var(--blue-deep)"/>
    <path d="M0,420 C250,500 600,480 886,400 L886,507 L0,507 Z" fill="var(--blue-mid)"/>
    <path d="M0,440 C150,505 400,500 886,460 L886,507 L0,507 Z" fill="var(--blue-bright)" opacity="0.5"/>
  </svg>
  <div class="band"></div>
  <h2 class="company">FERNHOLT<br>INTERNATIONAL LTD</h2>
</section>

</body>
</html>
```